International Clinical Software Company needs a new business card design

We are looking for a new business card design for our company that has recently expanded into the UK market, making us a multinational company.
After having rebranded our website and produced a new style guide, we are looking for a business card that is creative and attention grabbing, while being consistent with the style and colour scheme used on the new website, www.brookvale.example
We produce care management technology for the aged care market, but the main aspect we aim to communicate is the human element of our software, and the way it assists in providing better care for aged people, and stronger relationships between aged people and the staff that care for them.
Our current business card is a dark green with gold text, which makes the text quite difficult to read, not very aesthetically appealing and the colour scheme looks quite dated.
We would like something fresh and modern, that can still be colourful but doesn't use large blocks of dark colour, and uses the colours within our logo.
Something tying in with the leaves that are used in our logo could work quite nicely, along with the Autumn/Fall colours of soft greens, yellows and reds (also in our existing logo). However also happy to look at fresh, completely out of the box ideas we may not have yet considered.
Target Market(s)
The people that receive this business card work in the aged card or health industry and are either corporate/management level staff or clinical (Registered Nurses, care workers etc.)
Industry/Entity Type
Health Product
Contact Information for Business Card
Company Name - BrookvaleTech
Company locations: United Kingdom, Australia, New Zealand
Staff Details:
Staff name: Dermot Quill
Staff job title: Executive Chairman
Staff email: d.quill@brookvale.example
Office phone number: 01632 960418
Font styles to use
Other font styles liked:
- Calibri
Requirements
Must have
- Must include the BrookvaleTech brand name in it's current font
- Must include logo (3 leaves in gold circle)
- Must include Business Card Details
Nice to have
- Elements of gold
- White space
- Something autumn themed but not too cliched
Should not have
- No blue - used by a major competitor and we would like to differentiate from them
- Large blocks of dark green colour (the green that appears in our leaves on the logo on our current business card is the background colour and it is far too dark)

```html
<!DOCTYPE html>
<html lang="en">
<head>
<meta charset="utf-8">
<title>BrookvaleTech Business Card</title>
<link rel="stylesheet" href="https://fonts.googleapis.com/css2?family=Open+Sans:wght@300;400;600&display=swap">
<style>
  :root {
    --gold: #b5a170;
    --gold-text: #9c8652;
    --crimson: #a3102f;
    --white: #ffffff;
    --stage: #ebe8e2;
    --icon-green: #4d5a1e;
  }
  * { margin: 0; padding: 0; box-sizing: border-box; }
  html, body {
    width: 1200px; height: 1000px; overflow: hidden;
    background: var(--stage);
    font-family: "Open Sans", Calibri, Arial, sans-serif;
  }
  .card {
    position: absolute; left: 265px; width: 665px; height: 397px;
    border-radius: 22px; overflow: hidden;
    box-shadow: 0 4px 12px rgba(0,0,0,0.18);
  }
  .card--front { top: 73px; background: var(--white); }
  .card--back { top: 533px; background: var(--gold); }

  .brand-mark {
    position: absolute; border-radius: 50%;
  }
  .card--front .brand-mark {
    left: 288px; top: 48px; width: 88px; height: 88px;
    border: 3px solid var(--gold);
  }
  .brand-name {
    position: absolute; width: 100%; text-align: center;
    font-weight: 300; color: var(--gold-text); white-space: nowrap;
  }
  .card--front .brand-name { top: 158px; font-size: 40px; line-height: 56px; }

  .person-name {
    position: absolute; top: 258px; width: 100%; text-align: center;
    font-weight: 600; font-size: 22px; color: var(--crimson); letter-spacing: 0.5px;
  }
  .person-title {
    position: absolute; top: 288px; width: 100%; text-align: center;
    font-size: 15px; color: var(--gold-text);
  }
  .contact-line {
    position: absolute; top: 324px; width: 100%;
    display: flex; justify-content: center; align-items: center; gap: 26px;
    font-size: 15px; color: var(--gold-text);
  }
  .contact-item { display: flex; align-items: center; gap: 8px; }
  .contact-phone { letter-spacing: 2.5px; }
  .contact-icon { width: 22px; height: 22px; }
  .locations-band {
    position: absolute; left: 0; bottom: 0; width: 100%; height: 33px;
    background: var(--gold); color: var(--white);
    font-size: 15px; letter-spacing: 2px; text-align: center; line-height: 33px;
  }

  .card--back .brand-mark {
    left: 115px; top: 120px; width: 158px; height: 158px;
    border: 4px solid var(--white);
  }
  .card--back .brand-name {
    left: 285px; top: 184px; width: auto; text-align: left;
    font-size: 42px; line-height: 56px; color: var(--white);
  }
</style>
</head>
<body>
  <section class="card card--front">
    <div class="brand-mark"></div>
    <div class="brand-name">BrookvaleTech</div>
    <div class="person-name">DERMOT QUILL</div>
    <div class="person-title">Executive Chairman</div>
    <div class="contact-line">
      <span class="contact-item">
        <span class="contact-phone">01632 960418</span>
        <svg class="contact-icon" viewBox="0 0 22 22" aria-hidden="true">
          <circle cx="11" cy="11" r="9.5" fill="none" stroke="var(--icon-green)" stroke-width="1.5"/>
          <path d="M7.5 6.5c.6-.6 1.4-.5 1.8.1l.9 1.5c.3.5.2 1.1-.2 1.4l-.6.5c.6 1.3 1.6 2.3 2.9 2.9l.5-.6c.4-.4 1-.5 1.4-.2l1.5.9c.6.4.7 1.2.1 1.8l-.7.7c-.7.7-2 .7-3.4-.1-1.8-1-3.3-2.5-4.3-4.3-.8-1.4-.8-2.7-.1-3.4z" fill="var(--icon-green)"/>
        </svg>
      </span>
      <span class="contact-item">
        <svg class="contact-icon" viewBox="0 0 22 22" aria-hidden="true">
          <circle cx="11" cy="11" r="9.5" fill="none" stroke="var(--icon-green)" stroke-width="1.5"/>
          <rect x="6" y="7.5" width="10" height="7" fill="var(--icon-green)"/>
          <path d="M6 7.8l5 3.8 5-3.8" fill="none" stroke="#fff" stroke-width="1"/>
        </svg>
        <span>d.quill@brookvale.example</span>
      </span>
    </div>
    <div class="locations-band">United Kingdom, Australia, New Zealand</div>
  </section>

  <section class="card card--back">
    <div class="brand-mark"></div>
    <div class="brand-name">BrookvaleTech</div>
  </section>
</body>
</html>
```